Brennock transport business cards

Front of card, Looking for my logo on one side of the card

Back of card,
Brennock Transport Maintenance
Onsite Cars, Trucks & trailer maintenance and repairs
Gary Brennock
0452918406
Brennocktm@vexmail.test

```html
<!DOCTYPE html>
<html lang="en">
<head>
<meta charset="utf-8">
<title>Brennock Transport Maintenance – Business Cards</title>
<link rel="stylesheet" href="https://fonts.googleapis.com/css2?family=Montserrat:wght@400;600;700;800&family=Orbitron:wght@800&display=swap">
<style>
  :root {
    --backdrop: #cfd4d4;
    --card: #f1f1ef;
    --ink: #111111;
    --text-grey: #3c3c3c;
    --brand-blue: #2a78c8;
    --edge-blue: #2c74c4;
  }
  * { box-sizing: border-box; margin: 0; padding: 0; }
  html, body { width: 1200px; height: 881px; overflow: hidden; }
  body {
    background: var(--backdrop);
    font-family: "Montserrat", sans-serif;
    display: flex;
    flex-direction: column;
    align-items: center;
    justify-content: center;
    gap: 56px;
  }
  .card {
    position: relative;
    width: 620px;
    height: 354px;
    background: var(--card);
    border-bottom: 5px solid var(--edge-blue);
    box-shadow: 0 14px 30px rgba(0,0,0,0.18);
  }

  /* Brand lockup: plain circle + name */
  .brand {
    display: flex;
    align-items: center;
    gap: 12px;
  }
  .brand-dot {
    border-radius: 50%;
    background: var(--brand-blue);
    flex: none;
  }
  .brand-name {
    font-family: "Montserrat", sans-serif;
    font-weight: 800;
    color: var(--ink);
    text-transform: uppercase;
    line-height: 1;
  }
  .hotline {
    font-family: "Orbitron", sans-serif;
    font-weight: 800;
    color: var(--ink);
    line-height: 1;
    letter-spacing: 2px;
  }

  /* Front */
  .card-front .front-inner {
    position: absolute;
    inset: 0;
    display: flex;
    flex-direction: column;
    justify-content: center;
    align-items: center;
    gap: 26px;
  }
  .card-front .brand-dot { width: 46px; height: 46px; }
  .card-front .brand-name { font-size: 58px; }
  .card-front .hotline { font-size: 50px; }
  .card-front .rule { width: 480px; height: 3px; background: var(--brand-blue); }

  /* Back */
  .card-back .logo-block {
    position: absolute;
    left: 36px;
    top: 86px;
    width: 262px;
    display: flex;
    flex-direction: column;
    gap: 12px;
  }
  .card-back .brand-dot { width: 22px; height: 22px; }
  .card-back .brand-name { font-size: 30px; }
  .card-back .hotline { font-size: 26px; letter-spacing: 1px; }
  .card-back .divider {
    position: absolute;
    left: 318px;
    top: 74px;
    width: 2px;
    height: 142px;
    background: var(--brand-blue);
  }
  .contact {
    position: absolute;
    left: 342px;
    top: 96px;
  }
  .contact-name {
    font-weight: 700;
    font-size: 28px;
    color: var(--brand-blue);
    margin-bottom: 14px;
  }
  .contact-line {
    display: flex;
    align-items: center;
    gap: 8px;
    font-size: 15px;
    color: var(--text-grey);
    margin-bottom: 6px;
  }
  .contact-line svg { width: 14px; height: 14px; fill: var(--brand-blue); flex: none; }
  .services {
    position: absolute;
    left: 0;
    right: 0;
    bottom: 40px;
    text-align: center;
    font-size: 15px;
    line-height: 1.5;
    color: var(--text-grey);
  }
</style>
</head>
<body>

  <section class="card card-front">
    <div class="front-inner">
      <div class="brand">
        <span class="brand-dot"></span>
        <span class="brand-name">Brennock</span>
      </div>
      <div class="rule"></div>
      <div class="hotline">0452918406</div>
    </div>
  </section>

  <section class="card card-back">
    <div class="logo-block">
      <div class="brand">
        <span class="brand-dot"></span>
        <span class="brand-name">Brennock</span>
      </div>
      <div class="hotline">0452918406</div>
    </div>

    <div class="divider"></div>

    <div class="contact">
      <div class="contact-name">Gary Brennock</div>
      <div class="contact-line">
        <svg viewBox="0 0 16 16" aria-hidden="true"><path d="M3.6 1.2l2.3 2.7-1.4 1.6c.9 2 2.9 4 5 5l1.6-1.4 2.7 2.3-1.4 2.6C7.6 13.6 2.4 8.4 1 3.1z"/></svg>
        <span>0452918406</span>
      </div>
      <div class="contact-line">
        <svg viewBox="0 0 16 16" aria-hidden="true"><path d="M1 3h14v10H1z M2 4l6 5 6-5" fill="none" stroke="#2a78c8" stroke-width="1.6"/></svg>
        <span>Brennocktm@vexmail.test</span>
      </div>
    </div>

    <p class="services">
      Brennock Transport Maintenance<br>
      Onsite Cars, Trucks &amp; trailer maintenance and repairs
    </p>
  </section>

</body>
</html>
```